Form Crafters Business Card

Professional cosmetic surgery company, based in very exclusive area in London. High profiled clientele. Brand is very artistic, modern, state-of-the-art, safe. The best in the business. Celebrity clientele.

Form Crafter’s of London is a brand serving a discriminating and exclusive clientele who value personal service that is both intimate and high end. Our clients choose Form Crafters because of the relationships we share with all of our customers. The clients of Form Crafters have an equal partnership between customers, and very experienced, highly qualified medical professionals. This together provides you with a professional service that keeps you looking good and feeling good. It is a relationship based on honesty, compassion, loyalty and respect.
Form Crafter’s have provided services for internationally recognised celebrities, and other high profiled individuals.

The cards are used for networking at private, exclusive events with VIPs.

Target Market(s)

Professionals
Rich people

Industry/Entity Type

Professional Service

Contact Information for Business Card

Need double sided business card design for 4 people. Back of the business card needs to have contrast background to the front with butterfly watermark with services provided:
Hair Restoration surgery
Hair Loss treatments
Breast surgery
Rhinoplasty
Zelix Liposuction
Fat Grafting
Lumex & Fillers

Front of the business card needs to be a nice satin black.
with following information:
Talvan Desoruthy - name
Chief Executive - Job title

www.formcrafters-example.co.uk
talvan@formcrafters-example.co.uk
Phone: +44 (0)207 146 5327
Mobile: +44 (0)7491 825 436

The London Calder Infirmary
14 Pellmont Street | London | W1K 3TR
Off Dunmore Lane

All business cards have the same address, phone, website as Talvan's details.
Same details on the back of the business card as well.
The other cards have different name, job title, email, mobile number

Kerem Lutz - Name
Partner - Job Title
Former England International Cricketer - please include below job title

email: kerem@formcrafters-example.co.uk
mobile: +44(0)7862 514208

Dr Stellan Vastrel - Name
Plastic Surgeon - Job Title
drvastrel@formcrafters-example.co.uk
No mobile number

Dr Jon Torvick FRCS (please put FRCS in small font) - Name
Hair Restoration Surgeon - Job Title
drtorvick@formcrafters-example.co.uk
No mobile number

Colors
cedeec
85abd2
0655a3

Requirements
Must have
• The logo needs to be in a metallic finish
• Text needs to be striking
• nice background
• butterfly watermark on the back

```html
<!DOCTYPE html>
<html lang="en">
<head>
<meta charset="utf-8">
<title>Form Crafters Business Card</title>
<link rel="stylesheet" href="https://fonts.googleapis.com/css2?family=Open+Sans:wght@400;600&display=swap">
<style>
  :root {
    --backdrop: #d9dadc;
    --card-white: #ffffff;
    --card-black: #050505;
    --brand-blue: #0655a3;
    --mid-blue: #85abd2;
    --pale-blue: #cedeec;
    --accent-orange: #f07a12;
    --text-dark: #1a1a1a;
    --text-white: #ffffff;
    --text-grey: #b9c3cf;
  }
  * { margin: 0; padding: 0; box-sizing: border-box; }
  html, body {
    width: 1200px;
    height: 900px;
    overflow: hidden;
    background: var(--backdrop);
    font-family: "Open Sans", Arial, sans-serif;
  }
  .canvas { position: relative; width: 1200px; height: 900px; }
  .card {
    position: absolute;
    width: 540px;
    height: 330px;
    overflow: hidden;
    box-shadow: 0 10px 24px rgba(0, 0, 0, 0.25);
  }
  .card-front { left: 60px; top: 90px; background: var(--card-white); }
  .card-back { left: 600px; top: 480px; background: var(--card-black); }

  .brand {
    display: flex;
    align-items: center;
    gap: 10px;
    font-weight: 600;
    white-space: nowrap;
  }
  .brand-dot { border-radius: 50%; background: var(--accent-orange); flex: none; }

  /* Front */
  .card-front .brand {
    position: absolute;
    left: 32px;
    top: 40px;
    font-size: 28px;
    color: var(--brand-blue);
  }
  .card-front .brand-dot { width: 16px; height: 16px; }
  .address {
    position: absolute;
    left: 32px;
    top: 104px;
    font-size: 11.5px;
    line-height: 17px;
    color: var(--text-dark);
    font-style: normal;
  }
  .person {
    position: absolute;
    right: 32px;
    top: 72px;
    text-align: right;
  }
  .person-name { font-size: 20px; font-weight: 600; color: var(--brand-blue); }
  .person-title { font-size: 14px; color: var(--accent-orange); margin-top: 1px; }
  .contact-list {
    position: absolute;
    right: 32px;
    top: 150px;
    list-style: none;
    font-size: 13.5px;
    color: var(--text-dark);
  }
  .contact-list li { display: flex; align-items: center; gap: 8px; height: 22px; }
  .contact-list svg { width: 14px; height: 14px; flex: none; }
  .swoosh { position: absolute; left: 0; bottom: 0; width: 540px; height: 100px; }

  /* Back */
  .watermark {
    position: absolute;
    right: -60px;
    top: -40px;
    width: 300px;
    height: 300px;
    border-radius: 50%;
    background: radial-gradient(circle, rgba(133, 171, 210, 0.14), rgba(133, 171, 210, 0));
  }
  .card-back .brand {
    position: absolute;
    left: 0;
    right: 0;
    top: 46px;
    justify-content: center;
    font-size: 36px;
    color: var(--mid-blue);
  }
  .card-back .brand-dot { width: 20px; height: 20px; }
  .services {
    position: absolute;
    left: 40px;
    right: 40px;
    top: 122px;
    list-style: none;
    display: flex;
    flex-wrap: wrap;
    justify-content: center;
    gap: 4px 16px;
    font-size: 12px;
    color: var(--pale-blue);
  }
  .services li { white-space: nowrap; }
  .back-address {
    position: absolute;
    left: 0;
    right: 0;
    top: 200px;
    text-align: center;
    font-size: 11.5px;
    line-height: 17px;
    color: var(--text-grey);
    font-style: normal;
  }
  .back-web {
    position: absolute;
    left: 0;
    right: 0;
    top: 268px;
    text-align: center;
    font-size: 15px;
    letter-spacing: 4px;
    color: var(--text-white);
  }
</style>
</head>
<body>
<main class="canvas">

  <section class="card card-front" aria-label="Business card front">
    <div class="brand"><span class="brand-dot"></span>Form Crafters</div>

    <address class="address">
      The London Calder Infirmary<br>
      14 Pellmont Street | London | W1K 3TR<br>
      Off Dunmore Lane
    </address>

    <div class="person">
      <p class="person-name">Dr Stellan Vastrel</p>
      <p class="person-title">Plastic Surgeon</p>
    </div>

    <ul class="contact-list">
      <li>
        <svg viewBox="0 0 14 14"><path d="M7 1a4 4 0 0 0-4 4c0 3 4 8 4 8s4-5 4-8a4 4 0 0 0-4-4z" fill="none" stroke="#f07a12" stroke-width="1.6"/><circle cx="7" cy="5" r="1.3" fill="#f07a12"/></svg>
        Phone: +44 (0)207 146 5327
      </li>
      <li>
        <svg viewBox="0 0 14 14"><rect x="1" y="3" width="12" height="8.5" fill="none" stroke="#f07a12" stroke-width="1.3"/><path d="M1 3l6 5 6-5" fill="none" stroke="#f07a12" stroke-width="1.3"/></svg>
        drvastrel@formcrafters-example.co.uk
      </li>
      <li>
        <svg viewBox="0 0 14 14"><circle cx="7" cy="7" r="5.8" fill="none" stroke="#f07a12" stroke-width="1.3"/><path d="M1.2 7h11.6M7 1.2c-2.6 3-2.6 8.6 0 11.6M7 1.2c2.6 3 2.6 8.6 0 11.6" fill="none" stroke="#f07a12" stroke-width="1"/></svg>
        www.formcrafters-example.co.uk
      </li>
    </ul>

    <svg class="swoosh" viewBox="0 0 540 100" preserveAspectRatio="none" aria-hidden="true">
      <defs>
        <linearGradient id="swoosh-fill" x1="0" y1="0" x2="1" y2="0">
          <stop offset="0" stop-color="#0655a3"/>
          <stop offset="0.6" stop-color="#85abd2"/>
          <stop offset="1" stop-color="#cedeec"/>
        </linearGradient>
      </defs>
      <path d="M0 25 C 120 90, 360 92, 540 58 L540 100 L0 100 Z" fill="url(#swoosh-fill)"/>
    </svg>
  </section>

  <section class="card card-back" aria-label="Business card back">
    <div class="watermark" role="img" aria-label="Faint brand watermark area"></div>
    <div class="brand"><span class="brand-dot"></span>Form Crafters</div>

    <ul class="services">
      <li>Hair Restoration surgery</li>
      <li>Hair Loss treatments</li>
      <li>Breast surgery</li>
      <li>Rhinoplasty</li>
      <li>Zelix Liposuction</li>
      <li>Fat Grafting</li>
      <li>Lumex &amp; Fillers</li>
    </ul>

    <address class="back-address">
      The London Calder Infirmary<br>
      14 Pellmont Street | London | W1K 3TR | Off Dunmore Lane<br>
      Phone: +44 (0)207 146 5327
    </address>

    <p class="back-web">www.formcrafters-example.co.uk</p>
  </section>

</main>
</body>
</html>
```